Book title: Lanternfall: The spark of momentum!

This book is called: Lanternfall: The spark of momentum!

A guide to understanding the most popular types of coaching and how to find the perfect coach for you.
The coaching industry has exploded over the past few years as the demand for them has increased. With so many different types of coaches it can be intimidating and overwhelming to find the perfect one for you. To further complicate matters, you may experience times in your life when you require multiple coaches. {Book Title} aims to quite the noise and assist you in finding the perfect coach for you. In this book, you will learn more about the different types of coaching as well as meet a hand-picked selection of coaches from the most popular coaching niches. Each featured coach has provided an exercise designed to move you powerfully forward. We encourage you to work through each exercise so you may experience firsthand the power of working with these incredible coaches.

We would like a professional and simple design. See examples included. We would like to see blood orange included in the design, please see color pallets included as well.

Target Market(s)

Corporate professionals wanting to explore the various types of coaching industry

Industry/Entity Type

Coaching - Health, business, spiritual

Font styles to use
Serif

Colors
EE7325
F08F49
F5BC92
FAE3D3
FDF4ED

Requirements
Must have
• Please include book title: Lanternfall, Subtitle: The spark of momentum! Name of publishing company: Silver Meadow Publishing, Spaces for 8 author names on the front of the cover- Author Name
Nice to have
• A feminine yet corporate feel.
Should not have
• We don't want it

```html
<!DOCTYPE html>
<html lang="en">
<head>
<meta charset="UTF-8">
<title>Lanternfall: The spark of momentum!</title>
<link rel="stylesheet" href="https://fonts.googleapis.com/css2?family=EB+Garamond:wght@400;500&display=swap">
<style>
  :root {
    --page: #ffffff;
    --blood-orange: #df501a;
    --ink-light: #ffffff;
  }
  html, body {
    margin: 0;
    padding: 0;
    width: 1200px;
    height: 1200px;
    overflow: hidden;
    background: var(--page);
  }
  .canvas {
    position: relative;
    width: 1200px;
    height: 1200px;
    background: var(--page);
  }
  .cover {
    position: absolute;
    left: 241px;
    top: 61px;
    width: 719px;
    height: 1078px;
    background: var(--blood-orange);
    color: var(--ink-light);
    font-family: "EB Garamond", "Garamond", serif;
    text-transform: uppercase;
  }
  .rule {
    position: absolute;
    left: 77px;
    width: 564px;
    height: 4px;
  }
  .rule--top { top: 104px; }
  .rule--mid { top: 341px; }
  .rule--author { top: 792px; }
  .title {
    position: absolute;
    left: 0;
    width: 100%;
    margin: 0;
    text-align: center;
    font-weight: 400;
    font-size: 102px;
    line-height: 94px;
    letter-spacing: 0.06em;
  }
  .title { top: 118px; }
  .title span { display: block; }
  .subtitle {
    position: absolute;
    top: 390px;
    left: 0;
    width: 100%;
    margin: 0;
    text-align: center;
    font-weight: 400;
    font-size: 42px;
    line-height: 1;
    letter-spacing: 0.06em;
  }
  .publisher {
    position: absolute;
    top: 742px;
    left: 0;
    width: 100%;
    margin: 0;
    text-align: center;
    font-weight: 400;
    font-size: 31px;
    line-height: 1;
    letter-spacing: 0.07em;
  }
  .authors {
    position: absolute;
    top: 814px;
    left: 0;
    width: 100%;
    margin: 0;
    padding: 0;
    list-style: none;
    font-size: 27px;
    line-height: 29.5px;
    letter-spacing: 0.02em;
  }
  .author-row {
    display: flex;
    justify-content: center;
    gap: 32px;
  }
  .author-name { white-space: nowrap; }
</style>
</head>
<body>
  <div class="canvas">
    <section class="cover">
      <svg class="rule rule--top" viewBox="0 0 564 4" preserveAspectRatio="none" aria-hidden="true">
        <path d="M0 2 Q282 -1 564 2 Q282 5 0 2 Z" fill="var(--ink-light)"/>
      </svg>

      <h1 class="title"><span>Lantern</span><span>Fall</span></h1>

      <svg class="rule rule--mid" viewBox="0 0 564 4" preserveAspectRatio="none" aria-hidden="true">
        <path d="M0 2 Q282 -1 564 2 Q282 5 0 2 Z" fill="var(--ink-light)"/>
      </svg>

      <p class="subtitle">The Spark of Momentum!</p>

      <p class="publisher">Silver Meadow Publishing</p>

      <svg class="rule rule--author" viewBox="0 0 564 4" preserveAspectRatio="none" aria-hidden="true">
        <path d="M0 2 Q282 0 564 2 Q282 4 0 2 Z" fill="var(--ink-light)"/>
      </svg>

      <div class="authors">
        <div class="author-row">
          <span class="author-name">Author Name</span>
          <span class="author-name">Author Name</span>
          <span class="author-name">Author Name</span>
        </div>
        <div class="author-row">
          <span class="author-name">Author Name</span>
          <span class="author-name">Author Name</span>
          <span class="author-name">Author Name</span>
        </div>
        <div class="author-row">
          <span class="author-name">Author Name</span>
          <span class="author-name">Author Name</span>
        </div>
      </div>
    </section>
  </div>
</body>
</html>
```